Digital menu Skydiving company

Design Digital menu/pricelist for our company. It can have dynamic components. We are also looking for a Graphic design for all our projects. Our main goals are to look clean/sharp and professional. Information is in psd file

3 packages Violet Plunge, Meadow Journey, And Lantern Voyage. then we have addons and merchandise

Colors
0293ce
34a7d8
ffffff
fbee3f
3377b5
000000
f37122
ec1f27
e34197

Requirements
Must have
• Sorry If I couldn't get my vision across better, Please see really rough design idea attached. one large picture section that rotates through 3 or 4 pictures. then all the information down the bottom and on right (see menu pricelist attached)

```html
<!DOCTYPE html>
<html lang="en">
<head>
<meta charset="utf-8">
<title>Altura Skydive – Packages &amp; Pricing</title>
<link href="https://fonts.googleapis.com/css2?family=Montserrat:wght@400;700;800;900&display=swap" rel="stylesheet">
<style>
  :root{
    --sheet-bg:#4a4a4a;
    --white:#ffffff;
    --navy:#1d2a44;
    --card-bg:#050b1c;
    --blue:#0293ce;
    --blue-light:#34a7d8;
    --orange:#f37122;
    --red:#ec1f27;
    --pink:#e34197;
    --magenta:#e621b4;
    --grad-violet:linear-gradient(90deg,#2f8fd8 0%,#8a6fd0 55%,#e34197 100%);
    --grad-meadow:linear-gradient(90deg,#f37122 0%,#ef4a25 60%,#ec1f27 100%);
    --grad-lantern:linear-gradient(90deg,#e621b4 0%,#ea3a8a 55%,#ec1f27 100%);
  }
  *{box-sizing:border-box;margin:0;padding:0}
  html,body{width:828px;height:1200px;overflow:hidden;background:var(--sheet-bg)}
  body{font-family:"Montserrat",Arial,sans-serif;color:var(--white)}
  .sheet{position:relative;width:828px;height:1200px;background:var(--sheet-bg)}

  .board{position:absolute;left:112px;width:610px;height:342px;overflow:hidden;box-shadow:0 10px 18px rgba(0,0,0,.45)}
  .board--dusk{top:46px}
  .board--sky{top:425px}
  .board--wing{top:803px}

  .board-header{position:relative;height:41px;background:var(--white)}
  .brand{position:absolute;left:14px;top:9px;display:flex;align-items:center;gap:5px;color:var(--navy);font-weight:800;font-size:10px;line-height:1;letter-spacing:1px}
  .brand-dot{width:12px;height:12px;border-radius:50%;background:var(--navy)}
  .brand-name span{display:block}
  .brand-name span + span{font-size:7.5px;letter-spacing:2.6px;margin-top:2px}
  .board-title{position:absolute;left:155px;top:5px;font-size:27px;font-weight:800;letter-spacing:.6px;line-height:31px}
  .board--dusk .board-title{color:var(--blue)}
  .board--sky .board-title{color:var(--orange)}
  .board--wing .board-title{color:var(--magenta)}

  .scene{position:absolute;left:0;right:0;top:41px;bottom:0}
  .scene--dusk{background:linear-gradient(180deg,#b9cfe6 0%,#e9dcd0 30%,#f2c7a8 52%,#b98b77 62%,#6e5249 78%,#3e2f2e 100%)}
  .scene--sky{background:linear-gradient(180deg,#243d9a 0%,#3a5db8 45%,#7d9ad0 70%,#b07d6c 78%,#6f5a5a 90%,#4a4248 100%)}
  .scene--wing{background:linear-gradient(180deg,#5e6d82 0%,#c7d0dc 22%,#9fb0c6 38%,#8f7a72 52%,#6f5850 75%,#4a3e3c 100%)}

  .packages{position:absolute;left:281px;top:178px;display:flex;gap:5px}
  .card{width:103px;height:158px;border-radius:9px;background:var(--card-bg);overflow:hidden;display:flex;flex-direction:column;box-shadow:0 3px 8px rgba(0,0,0,.4)}
  .card--meadow,.card--lantern{margin-top:-2px;height:160px}
  .card-head{height:18px;text-align:center;font-size:6.4px;font-weight:800;line-height:1.08;padding-top:2px;letter-spacing:.2px}
  .card--violet .card-head,.card--violet .price{background:var(--grad-violet)}
  .card--meadow .card-head,.card--meadow .price{background:var(--grad-meadow)}
  .card--lantern .card-head,.card--lantern .price{background:var(--grad-lantern)}
  .tagline{text-align:center;font-size:4.3px;margin:5px 0 4px;letter-spacing:.1px}

  .features{list-style:none;padding:0 5px 0 5px}
  .feature{display:flex;align-items:flex-start;gap:3px;font-size:6.4px;font-weight:800;line-height:1.05;margin-bottom:4px}
  .card--violet .feature{margin-bottom:7px}
  .card--lantern .feature{margin-bottom:3.5px}
  .tick{flex:0 0 5px;width:5px;height:5px;margin-top:1px}
  .feature-label{flex:1}
  .feature-cost{font-size:4.6px;color:var(--blue-light);font-weight:700;margin-top:1px}

  .merch{padding:2px 6px 0 11px;font-size:6.6px;line-height:8.6px}
  .merch-row{display:flex;justify-content:space-between}

  .price{margin:auto auto 8px;padding:1px 6px 0;border-radius:10px;font-size:15px;font-weight:900;line-height:16px;letter-spacing:.2px}
</style>
</head>
<body>
<main class="sheet">

  <!-- Board 1 -->
  <section class="board board--dusk">
    <header class="board-header">
      <div class="brand"><span class="brand-dot"></span><div class="brand-name"><span>ALTURA</span><span>SKYDIVE</span></div></div>
      <h1 class="board-title">PACKAGES &amp; PRICING</h1>
    </header>
    <div class="scene scene--dusk" role="img" aria-label="Photo of a parachutist gliding over a canyon at sunset"></div>
    <div class="packages">
      <article class="card card--violet">
        <h2 class="card-head">VIOLET PLUNGE<br>16,000FT</h2>
        <p class="tagline">THE SKYDIVE IS NAKED, NOT YOU...</p>
        <ul class="features">
          <li class="feature"><svg class="tick" viewBox="0 0 10 10"><circle cx="5" cy="5" r="5" fill="#34a7d8"/><path d="M2.6 5.2l1.7 1.7 3.2-3.4" fill="none" stroke="#050b1c" stroke-width="1.4"/></svg><span class="feature-label">TANDEM SKYDIVE FROM 16,000FT MSL</span></li>
          <li class="feature"><svg class="tick" viewBox="0 0 10 10"><circle cx="5" cy="5" r="5" fill="#34a7d8"/><path d="M2.6 5.2l1.7 1.7 3.2-3.4" fill="none" stroke="#050b1c" stroke-width="1.4"/></svg><span class="feature-label">CERTIFICATE OF ACHIEVEMENT</span></li>
        </ul>
        <div class="merch">
          <div class="merch-row"><span>T-Shirt Short Sleeve</span><span>$20</span></div>
          <div class="merch-row"><span>T-Shirt Long Sleeve</span><span>$28</span></div>
          <div class="merch-row"><span>Sweat Shirts</span><span>$30</span></div>
          <div class="merch-row"><span>Hoodies</span><span>$38</span></div>
          <div class="merch-row"><span>Goggles from</span><span>$12</span></div>
        </div>
        <p class="price">$329</p>
      </article>
      <article class="card card--meadow">
        <h2 class="card-head">MEADOW JOURNEY<br>16,000FT</h2>
        <p class="tagline">SKYDIVE &amp; SHARE THE MEMORIES...</p>
        <ul class="features">
          <li class="feature"><svg class="tick" viewBox="0 0 10 10"><circle cx="5" cy="5" r="5" fill="#f37122"/><path d="M2.6 5.2l1.7 1.7 3.2-3.4" fill="none" stroke="#050b1c" stroke-width="1.4"/></svg><span class="feature-label">TANDEM SKYDIVE FROM 16,000FT MSL</span></li>
          <li class="feature"><svg class="tick" viewBox="0 0 10 10"><circle cx="5" cy="5" r="5" fill="#f37122"/><path d="M2.6 5.2l1.7 1.7 3.2-3.4" fill="none" stroke="#050b1c" stroke-width="1.4"/></svg><span class="feature-label">PHOTOS</span></li>
          <li class="feature"><svg class="tick" viewBox="0 0 10 10"><circle cx="5" cy="5" r="5" fill="#f37122"/><path d="M2.6 5.2l1.7 1.7 3.2-3.4" fill="none" stroke="#050b1c" stroke-width="1.4"/></svg><span class="feature-label">VIDEOS</span></li>
          <li class="feature"><svg class="tick" viewBox="0 0 10 10"><circle cx="5" cy="5" r="5" fill="#f37122"/><path d="M2.6 5.2l1.7 1.7 3.2-3.4" fill="none" stroke="#050b1c" stroke-width="1.4"/></svg><span class="feature-label">CERTIFICATE OF ACHIEVEMENT</span></li>
        </ul>
        <p class="price">$459</p>
      </article>
      <article class="card card--lantern">
        <h2 class="card-head">LANTERN VOYAGE<br>16,000FT</h2>
        <p class="tagline">FOR THE THRILL SEEKER...</p>
        <ul class="features">
          <li class="feature"><svg class="tick" viewBox="0 0 10 10"><circle cx="5" cy="5" r="5" fill="#34a7d8"/><path d="M2.6 5.2l1.7 1.7 3.2-3.4" fill="none" stroke="#050b1c" stroke-width="1.4"/></svg><span class="feature-label">TANDEM SKYDIVE FROM 16,000FT MSL</span><span class="feature-cost">$319</span></li>
          <li class="feature"><svg class="tick" viewBox="0 0 10 10"><circle cx="5" cy="5" r="5" fill="#34a7d8"/><path d="M2.6 5.2l1.7 1.7 3.2-3.4" fill="none" stroke="#050b1c" stroke-width="1.4"/></svg><span class="feature-label">PHOTOS</span><span class="feature-cost">$99</span></li>
          <li class="feature"><svg class="tick" viewBox="0 0 10 10"><circle cx="5" cy="5" r="5" fill="#34a7d8"/><path d="M2.6 5.2l1.7 1.7 3.2-3.4" fill="none" stroke="#050b1c" stroke-width="1.4"/></svg><span class="feature-label">VIDEOS</span><span class="feature-cost">$99</span></li>
          <li class="feature"><svg class="tick" viewBox="0 0 10 10"><circle cx="5" cy="5" r="5" fill="#34a7d8"/><path d="M2.6 5.2l1.7 1.7 3.2-3.4" fill="none" stroke="#050b1c" stroke-width="1.4"/></svg><span class="feature-label">EXTREME EXTRAS</span><span class="feature-cost">$50</span></li>
          <li class="feature"><svg class="tick" viewBox="0 0 10 10"><circle cx="5" cy="5" r="5" fill="#34a7d8"/><path d="M2.6 5.2l1.7 1.7 3.2-3.4" fill="none" stroke="#050b1c" stroke-width="1.4"/></svg><span class="feature-label">ALTURA SKYDIVE T-SHIRT</span></li>
          <li class="feature"><svg class="tick" viewBox="0 0 10 10"><circle cx="5" cy="5" r="5" fill="#34a7d8"/><path d="M2.6 5.2l1.7 1.7 3.2-3.4" fill="none" stroke="#050b1c" stroke-width="1.4"/></svg><span class="feature-label">CERTIFICATE OF ACHIEVEMENT</span></li>
        </ul>
        <p class="price">$499</p>
      </article>
    </div>
  </section>

  <!-- Board 2 -->
  <section class="board board--sky">
    <header class="board-header">
      <div class="brand"><span class="brand-dot"></span><div class="brand-name"><span>ALTURA</span><span>SKYDIVE</span></div></div>
      <h1 class="board-title">PACKAGES &amp; PRICING</h1>
    </header>
    <div class="scene scene--sky" role="img" aria-label="Photo of a tandem skydive pair in freefall under a deep blue sky above a canyon"></div>
    <div class="packages">
      <article class="card card--violet">
        <h2 class="card-head">VIOLET PLUNGE<br>16,000FT</h2>
        <p class="tagline">THE SKYDIVE IS NAKED, NOT YOU...</p>
        <ul class="features">
          <li class="feature"><svg class="tick" viewBox="0 0 10 10"><circle cx="5" cy="5" r="5" fill="#34a7d8"/><path d="M2.6 5.2l1.7 1.7 3.2-3.4" fill="none" stroke="#050b1c" stroke-width="1.4"/></svg><span class="feature-label">TANDEM SKYDIVE FROM 16,000FT MSL</span></li>
          <li class="feature"><svg class="tick" viewBox="0 0 10 10"><circle cx="5" cy="5" r="5" fill="#34a7d8"/><path d="M2.6 5.2l1.7 1.7 3.2-3.4" fill="none" stroke="#050b1c" stroke-width="1.4"/></svg><span class="feature-label">CERTIFICATE OF ACHIEVEMENT</span></li>
        </ul>
        <div class="merch">
          <div class="merch-row"><span>T-Shirt Short Sleeve</span><span>$20</span></div>
          <div class="merch-row"><span>T-Shirt Long Sleeve</span><span>$28</span></div>
          <div class="merch-row"><span>Sweat Shirts</span><span>$30</span></div>
          <div class="merch-row"><span>Hoodies</span><span>$38</span></div>
          <div class="merch-row"><span>Goggles from</span><span>$12</span></div>
        </div>
        <p class="price">$329</p>
      </article>
      <article class="card card--meadow">
        <h2 class="card-head">MEADOW JOURNEY<br>16,000FT</h2>
        <p class="tagline">SKYDIVE &amp; SHARE THE MEMORIES...</p>
        <ul class="features">
          <li class="feature"><svg class="tick" viewBox="0 0 10 10"><circle cx="5" cy="5" r="5" fill="#f37122"/><path d="M2.6 5.2l1.7 1.7 3.2-3.4" fill="none" stroke="#050b1c" stroke-width="1.4"/></svg><span class="feature-label">TANDEM SKYDIVE FROM 16,000FT MSL</span></li>
          <li class="feature"><svg class="tick" viewBox="0 0 10 10"><circle cx="5" cy="5" r="5" fill="#f37122"/><path d="M2.6 5.2l1.7 1.7 3.2-3.4" fill="none" stroke="#050b1c" stroke-width="1.4"/></svg><span class="feature-label">PHOTOS</span></li>
          <li class="feature"><svg class="tick" viewBox="0 0 10 10"><circle cx="5" cy="5" r="5" fill="#f37122"/><path d="M2.6 5.2l1.7 1.7 3.2-3.4" fill="none" stroke="#050b1c" stroke-width="1.4"/></svg><span class="feature-label">VIDEOS</span></li>
          <li class="feature"><svg class="tick" viewBox="0 0 10 10"><circle cx="5" cy="5" r="5" fill="#f37122"/><path d="M2.6 5.2l1.7 1.7 3.2-3.4" fill="none" stroke="#050b1c" stroke-width="1.4"/></svg><span class="feature-label">CERTIFICATE OF ACHIEVEMENT</span></li>
        </ul>
        <p class="price">$459</p>
      </article>
      <article class="card card--lantern">
        <h2 class="card-head">LANTERN VOYAGE<br>16,000FT</h2>
        <p class="tagline">FOR THE THRILL SEEKER...</p>
        <ul class="features">
          <li class="feature"><svg class="tick" viewBox="0 0 10 10"><circle cx="5" cy="5" r="5" fill="#34a7d8"/><path d="M2.6 5.2l1.7 1.7 3.2-3.4" fill="none" stroke="#050b1c" stroke-width="1.4"/></svg><span class="feature-label">TANDEM SKYDIVE FROM 16,000FT MSL</span><span class="feature-cost">$319</span></li>
          <li class="feature"><svg class="tick" viewBox="0 0 10 10"><circle cx="5" cy="5" r="5" fill="#34a7d8"/><path d="M2.6 5.2l1.7 1.7 3.2-3.4" fill="none" stroke="#050b1c" stroke-width="1.4"/></svg><span class="feature-label">PHOTOS</span><span class="feature-cost">$99</span></li>
          <li class="feature"><svg class="tick" viewBox="0 0 10 10"><circle cx="5" cy="5" r="5" fill="#34a7d8"/><path d="M2.6 5.2l1.7 1.7 3.2-3.4" fill="none" stroke="#050b1c" stroke-width="1.4"/></svg><span class="feature-label">VIDEOS</span><span class="feature-cost">$99</span></li>
          <li class="feature"><svg class="tick" viewBox="0 0 10 10"><circle cx="5" cy="5" r="5" fill="#34a7d8"/><path d="M2.6 5.2l1.7 1.7 3.2-3.4" fill="none" stroke="#050b1c" stroke-width="1.4"/></svg><span class="feature-label">EXTREME EXTRAS</span><span class="feature-cost">$50</span></li>
          <li class="feature"><svg class="tick" viewBox="0 0 10 10"><circle cx="5" cy="5" r="5" fill="#34a7d8"/><path d="M2.6 5.2l1.7 1.7 3.2-3.4" fill="none" stroke="#050b1c" stroke-width="1.4"/></svg><span class="feature-label">ALTURA SKYDIVE T-SHIRT</span></li>
          <li class="feature"><svg class="tick" viewBox="0 0 10 10"><circle cx="5" cy="5" r="5" fill="#34a7d8"/><path d="M2.6 5.2l1.7 1.7 3.2-3.4" fill="none" stroke="#050b1c" stroke-width="1.4"/></svg><span class="feature-label">CERTIFICATE OF ACHIEVEMENT</span></li>
        </ul>
        <p class="price">$499</p>
      </article>
    </div>
  </section>

  <!-- Board 3 -->
  <section class="board board--wing">
    <header class="board-header">
      <div class="brand"><span class="brand-dot"></span><div class="brand-name"><span>ALTURA</span><span>SKYDIVE</span></div></div>
      <h1 class="board-title">PACKAGES &amp; PRICING</h1>
    </header>
    <div class="scene scene--wing" role="img" aria-label="Photo from an aircraft wing strut looking down over a cloudy canyon landscape"></div>
    <div class="packages">
      <article class="card card--violet">
        <h2 class="card-head">VIOLET PLUNGE<br>16,000FT</h2>
        <p class="tagline">THE SKYDIVE IS NAKED, NOT YOU...</p>
        <ul class="features">
          <li class="feature"><svg class="tick" viewBox="0 0 10 10"><circle cx="5" cy="5" r="5" fill="#34a7d8"/><path d="M2.6 5.2l1.7 1.7 3.2-3.4" fill="none" stroke="#050b1c" stroke-width="1.4"/></svg><span class="feature-label">TANDEM SKYDIVE FROM 16,000FT MSL</span></li>
          <li class="feature"><svg class="tick" viewBox="0 0 10 10"><circle cx="5" cy="5" r="5" fill="#34a7d8"/><path d="M2.6 5.2l1.7 1.7 3.2-3.4" fill="none" stroke="#050b1c" stroke-width="1.4"/></svg><span class="feature-label">CERTIFICATE OF ACHIEVEMENT</span></li>
        </ul>
        <div class="merch">
          <div class="merch-row"><span>T-Shirt Short Sleeve</span><span>$20</span></div>
          <div class="merch-row"><span>T-Shirt Long Sleeve</span><span>$28</span></div>
          <div class="merch-row"><span>Sweat Shirts</span><span>$30</span></div>
          <div class="merch-row"><span>Hoodies</span><span>$38</span></div>
          <div class="merch-row"><span>Goggles from</span><span>$12</span></div>
        </div>
        <p class="price">$329</p>
      </article>
      <article class="card card--meadow">
        <h2 class="card-head">MEADOW JOURNEY<br>16,000FT</h2>
        <p class="tagline">SKYDIVE &amp; SHARE THE MEMORIES...</p>
        <ul class="features">
          <li class="feature"><svg class="tick" viewBox="0 0 10 10"><circle cx="5" cy="5" r="5" fill="#f37122"/><path d="M2.6 5.2l1.7 1.7 3.2-3.4" fill="none" stroke="#050b1c" stroke-width="1.4"/></svg><span class="feature-label">TANDEM SKYDIVE FROM 16,000FT MSL</span></li>
          <li class="feature"><svg class="tick" viewBox="0 0 10 10"><circle cx="5" cy="5" r="5" fill="#f37122"/><path d="M2.6 5.2l1.7 1.7 3.2-3.4" fill="none" stroke="#050b1c" stroke-width="1.4"/></svg><span class="feature-label">PHOTOS</span></li>
          <li class="feature"><svg class="tick" viewBox="0 0 10 10"><circle cx="5" cy="5" r="5" fill="#f37122"/><path d="M2.6 5.2l1.7 1.7 3.2-3.4" fill="none" stroke="#050b1c" stroke-width="1.4"/></svg><span class="feature-label">VIDEOS</span></li>
          <li class="feature"><svg class="tick" viewBox="0 0 10 10"><circle cx="5" cy="5" r="5" fill="#f37122"/><path d="M2.6 5.2l1.7 1.7 3.2-3.4" fill="none" stroke="#050b1c" stroke-width="1.4"/></svg><span class="feature-label">CERTIFICATE OF ACHIEVEMENT</span></li>
        </ul>
        <p class="price">$459</p>
      </article>
      <article class="card card--lantern">
        <h2 class="card-head">LANTERN VOYAGE<br>16,000FT</h2>
        <p class="tagline">FOR THE THRILL SEEKER...</p>
        <ul class="features">
          <li class="feature"><svg class="tick" viewBox="0 0 10 10"><circle cx="5" cy="5" r="5" fill="#34a7d8"/><path d="M2.6 5.2l1.7 1.7 3.2-3.4" fill="none" stroke="#050b1c" stroke-width="1.4"/></svg><span class="feature-label">TANDEM SKYDIVE FROM 16,000FT MSL</span><span class="feature-cost">$319</span></li>
          <li class="feature"><svg class="tick" viewBox="0 0 10 10"><circle cx="5" cy="5" r="5" fill="#34a7d8"/><path d="M2.6 5.2l1.7 1.7 3.2-3.4" fill="none" stroke="#050b1c" stroke-width="1.4"/></svg><span class="feature-label">PHOTOS</span><span class="feature-cost">$99</span></li>
          <li class="feature"><svg class="tick" viewBox="0 0 10 10"><circle cx="5" cy="5" r="5" fill="#34a7d8"/><path d="M2.6 5.2l1.7 1.7 3.2-3.4" fill="none" stroke="#050b1c" stroke-width="1.4"/></svg><span class="feature-label">VIDEOS</span><span class="feature-cost">$99</span></li>
          <li class="feature"><svg class="tick" viewBox="0 0 10 10"><circle cx="5" cy="5" r="5" fill="#34a7d8"/><path d="M2.6 5.2l1.7 1.7 3.2-3.4" fill="none" stroke="#050b1c" stroke-width="1.4"/></svg><span class="feature-label">EXTREME EXTRAS</span><span class="feature-cost">$50</span></li>
          <li class="feature"><svg class="tick" viewBox="0 0 10 10"><circle cx="5" cy="5" r="5" fill="#34a7d8"/><path d="M2.6 5.2l1.7 1.7 3.2-3.4" fill="none" stroke="#050b1c" stroke-width="1.4"/></svg><span class="feature-label">ALTURA SKYDIVE T-SHIRT</span></li>
          <li class="feature"><svg class="tick" viewBox="0 0 10 10"><circle cx="5" cy="5" r="5" fill="#34a7d8"/><path d="M2.6 5.2l1.7 1.7 3.2-3.4" fill="none" stroke="#050b1c" stroke-width="1.4"/></svg><span class="feature-label">CERTIFICATE OF ACHIEVEMENT</span></li>
        </ul>
        <p class="price">$499</p>
      </article>
    </div>
  </section>

</main>
</body>
</html>
```